Student Profile

I would like to create a profile of .a few scholars at a primary school in South Africa. The profile is attached. I would like to it to be visually appealing for donors and to be in the same vein as the Thabeng Academy PDF. Please also find our branding guide and our logo. I've also included a few pictures that I would like for you to include.

Target Market(s)

Potential donors

Industry/Entity Type

School

Requirements
Must have
• Colours from the branding guide, photos

```html
<!DOCTYPE html>
<html lang="en">
<head>
<meta charset="utf-8">
<title>Student Story Series – Thabeng Academy</title>
<link rel="stylesheet" href="https://fonts.googleapis.com/css2?family=Montserrat:ital,wght@0,300;0,900;1,700&family=Source+Sans+3:ital,wght@0,400;0,600;0,700;1,400;1,600;1,700&display=swap">
<style>
  :root{
    --stage:#2b2b2d;
    --paper:#ffffff;
    --navy:#13306a;
    --navy-deep:#0b1f4d;
    --ink-navy:#1a2a5e;
    --cyan:#0ba3e3;
    --brand-blue:#1f6fc0;
    --purple:#5a2e8c;
    --orange:#f7a11a;
    --green:#9cba2e;
    --yellow:#f9c51a;
    --body:#4a4a4a;
    --sans:"Source Sans 3", "Myriad Pro", Arial, sans-serif;
    --display:"Montserrat", Arial, sans-serif;
  }
  *{box-sizing:border-box;margin:0;padding:0}
  html,body{width:1200px;height:1200px;overflow:hidden;background:var(--stage)}
  .spread{position:absolute;left:16px;top:225px;width:1168px;height:750px;display:flex;gap:8px}
  .page{position:relative;width:580px;height:750px;background:var(--paper);overflow:hidden;font-family:var(--sans);color:var(--body)}
  .layer{position:absolute;left:0;top:0}

  /* cover page */
  .brand{position:absolute;left:28px;top:70px;display:flex;align-items:center;gap:12px}
  .brand-dot{width:40px;height:40px;border-radius:50%;background:var(--brand-blue);flex:none}
  .brand-name{font-family:var(--sans);font-weight:600;font-size:28px;color:var(--brand-blue);letter-spacing:.5px;text-transform:uppercase;line-height:1}
  .title-box{position:absolute;left:26px;top:175px;width:256px;height:249px;background:var(--cyan);padding:18px 0 0 16px;color:var(--ink-navy)}
  .title-box .t1{font-family:var(--display);font-weight:900;font-size:46px;line-height:.98;letter-spacing:-1px}
  .title-box .t2{font-family:var(--display);font-weight:900;font-size:57px;line-height:.98;letter-spacing:-2px}
  .title-box .t3{font-family:var(--display);font-weight:300;font-size:54px;line-height:.98;letter-spacing:1px}
  .starring{position:absolute;left:16px;top:183px;width:226px;height:32px;background:var(--ink-navy);transform:skewX(-22deg);display:flex;align-items:center;justify-content:center}
  .starring span{transform:skewX(22deg);font-family:var(--display);font-style:italic;font-weight:700;font-size:22px;color:#fff;letter-spacing:.5px}
  .title-box .motto{position:absolute;left:0;right:0;top:222px;text-align:center;font-style:italic;font-size:13px;color:#fff}
  .class-info{position:absolute;left:31px;top:434px;color:#fff}
  .class-info h2{font-size:17px;font-weight:700;line-height:1.2}
  .class-info .fav{font-size:12.5px;font-weight:700;color:var(--yellow);margin-top:4px}
  .class-info .why{font-size:12.5px;font-style:italic;font-weight:600;margin-top:2px}
  .contact{position:absolute;left:0;top:522px;list-style:none}
  .contact li{display:flex;align-items:center;height:26px;font-size:11px;color:var(--brand-blue);white-space:nowrap}
  .contact .tab{width:46px;height:16px;margin-right:8px;display:flex;align-items:center;justify-content:flex-end;padding-right:12px;clip-path:polygon(0 0,100% 0,86% 100%,0 100%);flex:none}
  .tab.orange{background:var(--orange)} .tab.purple{background:var(--purple)} .tab.sky{background:#4cc3f0}
  .contact strong{font-weight:700}
  .peer-quote{position:absolute;left:24px;top:612px;width:210px;font-size:13.4px;line-height:1.3;color:var(--purple)}
  .peer-quote .mark{font-family:Georgia,serif;font-weight:700;font-size:26px;color:var(--brand-blue);line-height:0;vertical-align:-7px}
  .peer-quote cite{display:block;font-size:9.5px;font-style:italic;font-weight:700;margin-top:8px;margin-left:24px}
  .divider{position:absolute;left:241px;top:527px;width:1px;height:195px;background:#c9c9c9}
  .intro{position:absolute;left:254px;top:572px;width:300px;font-size:11.2px;line-height:17px;text-align:justify}
  .intro .drop{float:left;font-family:var(--display);font-weight:300;font-size:60px;line-height:50px;color:var(--purple);margin:2px 6px 0 -2px}

  /* story page */
  .teacher-quote{position:absolute;right:26px;top:32px;width:290px;text-align:right;color:#fff;font-size:12px;line-height:16.2px}
  .teacher-quote .mark{font-family:Georgia,serif;font-weight:700;font-size:24px;line-height:0;vertical-align:-6px;margin-right:4px}
  .teacher-quote cite{display:block;margin-top:8px;font-size:9.5px;font-style:italic;font-weight:700;color:var(--orange)}
  .columns{position:absolute;left:26px;top:260px;width:528px;display:flex;gap:22px}
  .col{flex:1;font-size:9.6px;line-height:14.2px;text-align:justify}
  .col p+p{margin-top:7px}
</style>
</head>
<body>
<main class="spread">

  <section class="page cover">
    <svg class="layer" width="580" height="750" viewBox="0 0 580 750">
      <defs>
        <linearGradient id="playground" x1="0" y1="0" x2="1" y2="1">
          <stop offset="0" stop-color="#a7896a"/>
          <stop offset=".5" stop-color="#3d4d78"/>
          <stop offset="1" stop-color="#6d5c4a"/>
        </linearGradient>
      </defs>
      <polygon points="0,225 250,150 580,250 250,505 0,505" fill="var(--purple)"/>
      <polygon points="292,0 580,0 580,250 282,440" fill="url(#playground)" role="img" aria-label="Photo of a smiling schoolgirl in a navy school jacket on a playground swing"/>
      <polygon points="580,250 580,395 330,505 250,505" fill="var(--orange)"/>
      <polygon points="580,395 580,505 330,505" fill="var(--green)"/>
      <circle cx="416" cy="444" r="114" fill="#fff"/>
      <circle cx="416" cy="444" r="107" fill="#7d6a5a" role="img" aria-label="Photo of the student walking with her mother outdoors"/>
    </svg>

    <div class="brand"><span class="brand-dot"></span><span class="brand-name">Thabeng<br>Academy</span></div>

    <div class="title-box">
      <div class="t1">STUDENT</div>
      <div class="t2">STORY</div>
      <div class="t3">SERIES</div>
      <div class="starring"><span>STARRING: “NOMI”</span></div>
      <p class="motto">“Setting Dreams Free Since 2015”</p>
    </div>

    <div class="class-info">
      <h2>The Class of 2028</h2>
      <p class="fav">Favorite thing to learn at school:</p>
      <p class="why">Math because “it helps me to grow my brain”.</p>
    </div>

    <ul class="contact">
      <li><span class="tab orange"><svg width="12" height="12" viewBox="0 0 12 12"><circle cx="6" cy="6" r="5.3" fill="none" stroke="#fff" stroke-width="1"/><path d="M4 3.2l1 1.3-.6.8c.5.9 1.1 1.5 2 2l.8-.6 1.3 1-.6 1.1c-2.2-.3-4.1-2.2-4.4-4.4z" fill="#fff"/></svg></span>+27 11 555 0142</li>
      <li><span class="tab purple"><svg width="12" height="12" viewBox="0 0 12 12"><circle cx="6" cy="6" r="5.3" fill="none" stroke="#fff" stroke-width="1"/><rect x="3" y="4" width="6" height="4.2" fill="none" stroke="#fff" stroke-width=".9"/><path d="M3 4l3 2.4L9 4" fill="none" stroke="#fff" stroke-width=".9"/></svg></span>fundpotential@thabengacademy.org</li>
      <li><span class="tab sky"><svg width="12" height="12" viewBox="0 0 12 12"><circle cx="6" cy="6" r="5.3" fill="none" stroke="#fff" stroke-width="1"/><ellipse cx="6" cy="6" rx="2" ry="4" fill="none" stroke="#fff" stroke-width=".8"/><path d="M2 6h8" stroke="#fff" stroke-width=".8"/></svg></span>www.<strong>thabengacademy</strong>.org</li>
    </ul>

    <blockquote class="peer-quote"><span class="mark">“</span> Nomi shows compassion to other scholars. She says “sorry” if someone feels sad. She is also very curious, she’s always asking questions in class. <span class="mark">”</span>
      <cite>- Kagiso, Grade 1 Scholar</cite>
    </blockquote>

    <div class="divider"></div>

    <p class="intro"><span class="drop">N</span>omsa, or Nomi, as she likes to be called, loves to read. Her favourite book is Bobo’s Big Sister by Amy Holt. Nomi’s vivid imagination and confidence (she loves playing teacher too) thrive thanks to the safe, nurturing and containing environment at Thabeng Academy. Nomi feels seen and heard: “My teachers always teach me and they believe in me and tell me every chance they get.” Nomi’s confidence is a skill she feels she’s honed at Thabeng Academy. It’s certainly love and respect that has allowed Nomi to blossom.</p>
  </section>

  <section class="page story">
    <svg class="layer" width="580" height="750" viewBox="0 0 580 750">
      <defs>
        <linearGradient id="navyWave" x1="0" y1="0" x2="1" y2="1">
          <stop offset="0" stop-color="var(--navy)"/>
          <stop offset="1" stop-color="var(--navy-deep)"/>
        </linearGradient>
      </defs>
      <rect x="0" y="0" width="300" height="260" fill="#8a6e5a" role="img" aria-label="Photo of the student's mother smiling in a knitted cap beside the playground"/>
      <path d="M140 0H580V248Q420 212 262 190Q200 90 140 0Z" fill="url(#navyWave)"/>
      <path d="M0 232Q120 184 240 178Q420 182 580 238V258Q420 210 240 200Q120 204 0 252Z" fill="var(--orange)"/>
      <path d="M0 252Q120 204 240 200Q420 210 580 258V280H0Z" fill="#fff"/>
      <circle cx="232" cy="182" r="72" fill="#fff"/>
      <circle cx="232" cy="182" r="66" fill="#3a4a72" role="img" aria-label="Photo of the student in her school jacket"/>

      <path d="M250 750Q360 680 430 655Q510 625 580 612V600Q500 610 420 640Q330 675 230 750Z" fill="var(--orange)"/>
      <path d="M262 750Q370 684 440 660Q515 632 580 622V750Z" fill="url(#navyWave)"/>
      <circle cx="370" cy="670" r="68" fill="#fff"/>
      <circle cx="370" cy="670" r="62" fill="#7a4a52" role="img" aria-label="Photo of mother and daughter together at the playground climbing frame"/>
    </svg>

    <blockquote class="teacher-quote"><span class="mark">“</span>Nomi demonstrates excellence in her school work. She displays grit and tries until she gets it right; she is loving, shows compassion, and invites other scholars to play with her. She is one of the top scholars in my class – always eager to learn new things and is excellent at solving problems and overcoming challenges
      <cite>-Ms Dineo, Grade 1 Teacher</cite>
    </blockquote>

    <div class="columns">
      <div class="col">
        <p>At only six years old, Nomi says she has learned to love herself and others more. She brings this emotional attunement—along with the other critical knowledge and skills that she has gained at Thabeng—to her life experiences both within and outside of school.</p>
        <p>Nomi lives in a two-room house on 3rd Avenue in Alexandra Township with her mother, Grace, and two brothers, Sipho and Lwazi.</p>
        <p>While Grace earns enough to send her children to school and pay for the transport there, there isn’t much left and it is her alone who bears the cost of raising children. Grace’s husband was in an accident and he is no longer able to work as a builder. However, Grace is determined to send her three children to private schools like Thabeng Academy because local government schools are no alternatives. Grace’s hopes and dreams for her children arise from the deep love she feels for them as well as her own thwarted schooling dreams.</p>
        <p>“I was always number one in my class, and I especially loved accounting, but my mother didn’t really understand,” says Grace. Grace grew up hungry and said she didn’t get much adult support and encouragement. She dropped out in Grade 10, but still looked for piece work to support her studies. Grace moved to Johannesburg from Limpopo with her partner at the time to seek a new life. It was harder than she expected, compounded by her partner’s incapacity to work due to illness. Grace supported them both on a domestic worker’s salary.</p>
        <p>Tenacious little Nomi loves her mom and cherishes the time they spend reading books and doing Nomi’s math homework. “My mom tells me I can be anything I want to be.”</p>
      </div>
      <div class="col">
        <p>Indeed, Nomi wants to be many things. She wants to be a chef to help her mom with the cooking and, she wants to teach. She says her students will attend Highveld University after they finish school! Currently, Nomi enjoys helping other scholars with their class work, especially those struggling with math.</p>
        <p>After Nomi herself completes her university studies, she wants to live in Cape Town. “Cape Town makes me feel very happy,” she says.</p>
        <p>A university preparatory school located in the Alexandra Township of Johannesburg, South Africa, Thabeng Academy not only equips its scholars with the tools they need to achieve academic success, but also provides them with the skills necessary to succeed in life. This includes intentionally creating a nurturing and enabling environment where respect for oneself and others, self-confidence, and resiliency are equally developed and valued alongside the key learning and academic skills that are foundational for students on the path to university. “Thabeng Academy was founded so that children like Nomi can dream with their eyes wide opened! We are delighted to watch Nomi and her peers grow into such thoughtful and intelligent little beings”, says Thabeng Academy co-founder Lerato Mokoena-Hart</p>
      </div>
    </div>
  </section>

</main>
</body>
</html>
```